creative menu design for a fun taco restaurant

menu design for taco restaurant.
graphically creative. handwritten edgy style.
logo with current writing attached.
--for creative inspiration similar to what I am looking for go to :
Clipfolio -- Dwight Okafor @harbor482 -taco menu board
menu has create your own taco and burrito
and a cocktail/ beer menu
1970's inspired. should be FUN

Target Market(s)

20-40 milliners and gen z

Colors
f37022
9bcb3c
fbed22
1196d0
ec1f27

Requirements
Must have
• colorful
images
playful/ fun--it's TACOS
Nice to have
• graphics, handwritten, use of colors, 1970's-60's font
Should not have
• slick food photos
faded photos drawings are ok

```html
<!DOCTYPE html>
<html lang="en">
<head>
<meta charset="utf-8">
<title>Sunny Taco Menu Board</title>
<link href="https://fonts.googleapis.com/css2?family=Bagel+Fat+One&family=Bungee&family=Anton&family=Oswald:wght@500;600&family=Open+Sans:wght@400;700&family=Kalam:wght@700&family=Michroma&family=Pacifico&display=swap" rel="stylesheet">
<style>
  :root{
    --cream:#fcebc2;
    --orange:#f37022;
    --orange-soft:#f4904a;
    --green:#9bcb3c;
    --green-soft:#b3d25a;
    --yellow:#fbed22;
    --blue:#1196d0;
    --teal:#4fc3c0;
    --red:#ec1f27;
    --red-soft:#ef6445;
    --ink:#111;
  }
  *{box-sizing:border-box;margin:0;padding:0}
  html,body{width:1200px;height:729px;overflow:hidden;background:var(--cream)}
  .board{position:relative;width:1200px;height:729px;overflow:hidden;background:var(--cream);font-family:"Open Sans",sans-serif;color:var(--ink)}
  .abs{position:absolute}
  .backdrop{position:absolute;inset:0}
  .center{display:flex;flex-direction:column;align-items:center;justify-content:center;text-align:center}
  ul{list-style:none}

  .groovy{font-family:"Bagel Fat One",cursive;font-weight:400;color:var(--yellow);-webkit-text-stroke:1.6px var(--ink);paint-order:stroke fill;text-shadow:1px 3px 0 var(--ink);line-height:1;white-space:nowrap;letter-spacing:.5px}
  .blocky{font-family:"Bungee",sans-serif;font-weight:400;color:var(--yellow);-webkit-text-stroke:1px var(--ink);text-shadow:2px 3px 0 var(--ink);line-height:1.05;letter-spacing:-1px;transform:scaleY(1.22)}
  .jag{background:var(--yellow);clip-path:polygon(3% 4%,40% 0,70% 3%,100% 0,97% 30%,100% 60%,96% 100%,60% 97%,30% 100%,0 96%,3% 60%,0 30%)}

  /* brand */
  .brand{left:92px;top:80px;width:170px;height:110px}
  .brand-dot{width:26px;height:26px;border-radius:50%;background:var(--orange);margin-bottom:8px}
  .brand-name{font-family:"Oswald",sans-serif;font-weight:600;font-size:34px;color:var(--red);letter-spacing:1px}
  .contact{left:36px;top:280px;width:250px;font-family:"Kalam",cursive;font-weight:700;font-size:21px;line-height:1.2}

  /* build your own */
  .byo-title{left:430px;top:30px;width:420px;height:62px;font-size:44px}
  .step{height:36px;font-family:"Anton",sans-serif;font-size:20px;color:var(--yellow);letter-spacing:.3px;flex-direction:row;gap:14px}
  .step-1{left:342px;top:102px;width:165px}
  .step-2{left:548px;top:104px;width:175px}
  .step-3{left:790px;top:104px;width:155px}
  .vibe{left:348px;top:146px;width:148px;height:180px;justify-content:space-around;padding:6px 0}
  .vibe .v1{font-family:"Oswald",sans-serif;font-weight:500;font-size:25px}
  .vibe .v2{font-family:"Michroma",sans-serif;font-size:19px}
  .vibe .v3{font-family:"Oswald",sans-serif;font-weight:500;font-size:24px;letter-spacing:1px}
  .vibe .v4{font-family:"Pacifico",cursive;font-size:22px}
  .feeling{position:absolute;background:var(--yellow);border-radius:50%;font-weight:700;font-size:14px;line-height:1.2}
  .free{left:763px;top:146px;width:36px;height:192px;font-family:"Oswald",sans-serif;font-weight:500;font-size:17px;color:var(--yellow);writing-mode:vertical-rl;transform:rotate(180deg)}
  .top-box{left:798px;top:140px;width:162px;height:102px;font-size:13px;line-height:1.25}
  .dairy-box{left:800px;top:252px;width:160px;height:66px;font-size:13px;line-height:1.25}
  .box-head{font-family:"Oswald",sans-serif;font-weight:500;font-size:17px;letter-spacing:.5px}
  .guac{left:800px;top:330px;width:155px;height:22px;font-family:"Oswald",sans-serif;font-weight:500;font-size:16px;letter-spacing:.5px}

  /* birria */
  .birria-head{left:1008px;top:52px;width:162px;height:96px;font-size:34px}
  .birria-list{left:1012px;top:162px;width:152px;height:118px;font-weight:700;font-size:14px;gap:9px}
  .note{font-family:serif;font-weight:400;font-size:8px;font-style:italic;align-self:flex-end;margin:-9px 6px -4px 0}

  /* sides */
  .sides-head{left:58px;top:444px;width:180px;height:52px;font-size:38px}
  .sides-list{left:36px;top:530px;width:228px;height:142px;font-weight:700;font-size:14px;gap:6px}

  /* drinks */
  .drinks-head{left:362px;top:422px;width:160px;height:54px;font-size:36px}
  .drinks-list{left:360px;top:490px;width:165px;height:150px;font-weight:700;font-size:14px;gap:7px}

  /* cocktails */
  .ck-head{left:690px;top:406px;width:380px;height:56px;font-size:36px}
  .menu-block{font-size:13px;line-height:1.22}
  .specialty{left:602px;top:472px;width:212px;height:98px}
  .marg{left:632px;top:582px;width:168px;height:112px}
  .frozen{left:812px;top:508px;width:132px;height:156px;background:var(--yellow);border-radius:50%}
  .beer{left:962px;top:482px;width:186px;height:206px;justify-content:space-around}
</style>
</head>
<body>
<main class="board">
  <svg class="backdrop" width="1200" height="729" viewBox="0 0 1200 729" aria-hidden="true">
    <polygon points="0,0 48,0 130,420 60,430 0,120" fill="var(--teal)"/>
    <polyline points="10,0 50,110 30,300 90,430" fill="none" stroke="var(--blue)" stroke-width="5"/>
    <polygon points="50,0 300,0 285,370 230,450 140,300" fill="var(--teal)"/>
    <polygon points="300,0 320,0 320,500 305,500" fill="var(--blue)"/>
    <polygon points="360,360 400,360 385,400 360,400" fill="var(--teal)"/>
    <polygon points="285,620 370,640 380,729 300,729" fill="var(--teal)"/>
    <polyline points="290,630 370,655 375,729" fill="none" stroke="var(--blue)" stroke-width="5"/>
    <polygon points="410,680 450,729 415,729" fill="var(--teal)"/>
    <polygon points="1000,330 1060,330 1070,729 1020,729" fill="var(--teal)"/>
    <polygon points="1110,330 1150,320 1200,729 1150,729" fill="var(--teal)"/>
    <polyline points="1120,340 1160,330 1195,729" fill="none" stroke="var(--blue)" stroke-width="5"/>
    <polyline points="1070,345 1090,350 1110,729" fill="none" stroke="var(--blue)" stroke-width="4"/>
    <polygon points="1140,0 1200,0 1200,60" fill="var(--teal)"/>

    <polygon points="300,14 960,8 1000,30 992,365 900,378 310,365 298,200" fill="var(--orange-soft)"/>
    <polyline points="320,20 990,16 985,330 960,375 440,360 300,355" fill="none" stroke="var(--orange)" stroke-width="4"/>
    <polygon points="425,32 840,28 850,80 430,92" fill="var(--green)"/>
    <path d="M332 100 L512 98 L505 140 L340 142 L325 120Z" fill="var(--ink)"/>
    <path d="M540 102 L720 100 L728 140 L548 142 L555 120Z" fill="var(--ink)"/>
    <path d="M775 102 L950 102 L960 128 L948 140 L790 140 L780 120Z" fill="var(--ink)"/>
    <path d="M763 145 L800 150 L800 338 L770 340 L762 300Z" fill="var(--ink)"/>
    <g fill="var(--green)">
      <rect x="510" y="200" width="14" height="34"/><rect x="500" y="210" width="36" height="13"/>
      <rect x="733" y="216" width="14" height="34"/><rect x="722" y="226" width="36" height="13"/>
    </g>

    <rect x="995" y="28" width="200" height="287" fill="var(--green-soft)"/>
    <rect x="1000" y="36" width="190" height="274" fill="none" stroke="var(--green)" stroke-width="3"/>
    <polygon points="1005,50 1172,46 1168,145 1010,150" fill="var(--orange)"/>

    <polygon points="15,415 275,385 280,720 20,712" fill="var(--green-soft)"/>
    <polyline points="20,420 270,395 275,718" fill="none" stroke="var(--green)" stroke-width="3"/>
    <polygon points="55,444 238,438 240,494 60,500" fill="var(--orange)"/>

    <path d="M400 420 C450 370 540 380 552 470 C560 560 545 680 450 690 C360 700 320 620 330 520 C335 470 360 440 400 420Z" fill="var(--red-soft)"/>
    <path d="M390 430 C450 380 535 385 545 470 C556 560 540 675 455 682 C370 690 335 620 340 520" fill="none" stroke="var(--red)" stroke-width="3"/>
    <polygon points="362,424 522,418 526,472 368,478" fill="var(--green)"/>

    <path d="M640 410 C700 370 900 380 1050 395 C1160 405 1195 470 1190 560 C1185 650 1140 710 1000 706 C850 702 700 712 630 680 C575 650 570 520 585 470 C595 440 610 425 640 410Z" fill="var(--red-soft)"/>
    <path d="M620 430 C700 375 1000 385 1110 420 C1195 450 1190 560 1180 620 C1170 690 1050 705 900 700 C760 696 640 705 600 650" fill="none" stroke="var(--red)" stroke-width="3"/>
    <polygon points="690,412 1068,400 1065,455 695,462" fill="var(--orange)"/>
    <circle cx="572" cy="400" r="18" fill="var(--red-soft)" stroke="var(--red)" stroke-width="3"/>
    <circle cx="560" cy="680" r="26" fill="var(--red-soft)" stroke="var(--red)" stroke-width="3"/>

    <ellipse cx="172" cy="312" rx="136" ry="70" fill="var(--yellow)" fill-opacity=".5" stroke="var(--yellow)" stroke-width="4"/>
  </svg>

  <div class="abs brand center">
    <span class="brand-dot"></span>
    <span class="brand-name">Sunny Taco</span>
  </div>
  <div class="abs contact center">
    <span>sunnytacoshop.com</span>
    <span>insta @sunnytaco</span>
    <span>phone 555</span>
  </div>

  <h1 class="abs byo-title groovy center">Build Your Own</h1>
  <div class="abs step step-1 center"><span>1</span><span>PICK YOUR VIBE</span></div>
  <div class="abs step step-2 center"><span>2</span><span>PICK YOUR FEELING</span></div>
  <div class="abs step step-3 center"><span>3</span><span>TOP IT</span></div>

  <div class="abs vibe jag center">
    <span class="v1">SOFT TACO</span>
    <span class="v2">BURRITO</span>
    <span class="v3">BOWL</span>
    <span class="v4">Salad</span>
  </div>

  <div class="feeling center" style="left:540px;top:142px;width:86px;height:72px">CUBAN<br>CHICKEN</div>
  <div class="feeling center" style="left:636px;top:160px;width:86px;height:72px">KOREAN<br>BEEF</div>
  <div class="feeling center" style="left:540px;top:224px;width:88px;height:84px">BANG<br>BANG<br>SHRIMP</div>
  <div class="feeling center" style="left:636px;top:244px;width:80px;height:66px">CHILE<br>PORK</div>

  <div class="abs free center">PICK THREE FREE!!</div>
  <div class="abs top-box jag center">
    <span class="box-head">TOPPINGS</span>
    <span>pico de gallo salsa</span><span>lettuce</span><span>adovada rice</span><span>black beans</span>
  </div>
  <div class="abs dairy-box jag center">
    <span class="box-head">DAIRY</span>
    <span>sour cream</span><span>cheese</span>
  </div>
  <div class="abs guac jag center">GUAC?&nbsp; ADD&nbsp; .99</div>

  <h2 class="abs birria-head blocky center">BIRRIA<br>TACOS</h2>
  <ul class="abs birria-list jag center">
    <li>BEEF BARRIOA</li>
    <li>QUESABIRRIA</li>
    <li>GOAT BIRRIA</li>
    <li class="note">*limited availability</li>
    <li>VEGAN BIRRIA</li>
  </ul>

  <h2 class="abs sides-head blocky center">SIDES</h2>
  <ul class="abs sides-list jag center">
    <li>GUAC AND CHIPS</li>
    <li>SALSA AND CHIPS</li>
    <li>SWEET PLANTAINS</li>
    <li>TOSTOTONES <i style="font-family:serif;font-weight:400">w/</i>GARLIC</li>
    <li>RICE AND BEANS</li>
  </ul>

  <h2 class="abs drinks-head groovy center">Drinks</h2>
  <ul class="abs drinks-list jag center">
    <li>FIZZITOS</li>
    <li>SUGAR COLA</li>
    <li>WATER</li>
    <li>LEMONADE</li>
  </ul>

  <h2 class="abs ck-head groovy center">Cocktails and Beer</h2>
  <div class="abs specialty jag center menu-block">
    <span class="box-head">SPECIALTY&nbsp; COCKTAILS</span>
    <span>cocktail 1</span><span>cocktail 2</span><span>cocktail 3</span>
  </div>
  <div class="abs marg jag center menu-block">
    <span class="box-head">MARGARITA</span>
    <span>specialty</span><span>margarita 1</span><span>margarita 2</span><span>margarita 3</span>
  </div>
  <div class="abs frozen center menu-block">
    <span class="box-head">FROZEN</span>
    <span>flavor 1</span><span>flavor 2</span>
    <span style="margin-top:14px">sm</span><span>large</span>
  </div>
  <div class="abs beer jag center menu-block">
    <div class="center"><span class="box-head">BEER&nbsp; ON&nbsp; TAP</span><span>beer 1</span><span>beer 2</span></div>
    <div class="center"><span class="box-head">BOTTLED&nbsp; BEER</span><span>beer 1</span><span>beer 2</span></div>
  </div>
</main>
</body>
</html>
```